Company Stationary

I'd like a template to use for company stationery. We frequently write short 1 - 2 page Word documents (which we save as PDF) to clients and prospects and the presentation is boring and doesn't look professional. I am looking for a Word template that will convey a better sense of professionalism. The design should include our logo (attached) but be simple and elegant. It should save nicely as a PDF, since that is how we will send the files via email.

Target Market(s)

Financial Institutions

Industry/Entity Type

Financial Service

Font styles to use
Serif

Colors

Designer to choose colors to be used in the design.

Requirements
Must have
• Simple design. Needs to be subtle. I don't want the design to be more interesting than the message we are writing.
Nice to have
• When the reader sees it, I want them to feel they are reading something published by a large, very successful company.
Should not have
• Not overpowering design and colors.

```html
<!DOCTYPE html>
<html lang="en">
<head>
<meta charset="utf-8">
<title>Veridane — Letterhead</title>
<link rel="stylesheet" href="https://fonts.googleapis.com/css2?family=Open+Sans:wght@400;700&display=swap">
<style>
  :root {
    --ink: #111111;
    --accent: #ee2428;
    --charcoal: #2b2f33;
    --watermark: #f1f1f1;
    --paper: #ffffff;
  }
  html, body {
    margin: 0;
    padding: 0;
    width: 1000px;
    height: 1200px;
    overflow: hidden;
    background: var(--paper);
  }
  .letterhead {
    position: relative;
    width: 1000px;
    height: 1200px;
    background: var(--paper);
    font-family: "Open Sans", Arial, sans-serif;
    color: var(--ink);
  }
  .brand {
    position: absolute;
    left: 52px;
    top: 52px;
    display: flex;
    align-items: center;
    gap: 14px;
  }
  .brand-mark {
    width: 22px;
    height: 22px;
    background: var(--accent);
  }
  .brand-name {
    font-size: 50px;
    font-weight: 700;
    letter-spacing: 1px;
    line-height: 1;
    color: var(--ink);
  }
  .contact {
    position: absolute;
    left: 750px;
    top: 40px;
    height: 94px;
    padding-left: 27px;
    border-left: 2px solid var(--accent);
    font-size: 16px;
    line-height: 20px;
  }
  .contact p { margin: 0; }
  .contact .label { color: var(--accent); }
  .contact address {
    font-style: normal;
    margin-top: 18px;
  }
  .watermark {
    position: absolute;
    left: 0;
    right: 0;
    top: 590px;
    text-align: center;
    font-size: 110px;
    font-weight: 700;
    letter-spacing: 4px;
    color: var(--watermark);
    line-height: 1;
    user-select: none;
  }
  .footer-band {
    position: absolute;
    left: 0;
    bottom: 0;
    width: 1000px;
    height: 25px;
    display: flex;
  }
  .footer-band .band-dark { width: 407px; background: var(--charcoal); }
  .footer-band .band-accent { flex: 1; background: var(--accent); }
</style>
</head>
<body>
  <main class="letterhead">
    <header>
      <div class="brand">
        <span class="brand-mark"></span>
        <span class="brand-name">Veridane</span>
      </div>
      <div class="contact">
        <p><span class="label">P:</span> (555) 014-2287</p>
        <p><span class="label">E:</span> info@veridane.com</p>
        <address>418 Linden Avenue<br>Fairhaven, NJ 07099</address>
      </div>
    </header>
    <div class="watermark" aria-hidden="true">Veridane</div>
    <footer class="footer-band">
      <span class="band-dark"></span>
      <span class="band-accent"></span>
    </footer>
  </main>
</body>
</html>
```